A Weather Forecasting Site needs designs

We need a website design for our new venture which is a weather forecasting website. This website should have the latest design trends.

Menu
Weather, Maps, Videos and Photos

The home page requirements are as follows:
- Search Bar
- Local Weather
- Weather forecast of major cities in the World
Favorite locations
- Space for ADs
- Email signup

Weather Details page
This page will be redirected from the home page when you click on any of the weather forecast section

We are open to all kinds of designs and ideas. Feel free to you colors which suite your design.

```html
<!DOCTYPE html>
<html lang="en">
<head>
<meta charset="utf-8">
<title>A Weather Forecasting</title>
<link rel="stylesheet" href="https://fonts.googleapis.com/css2?family=Poppins:wght@400;500;600;700&family=Roboto:wght@400;500;700&display=swap">
<style>
:root{
  --navy:#1c3050;
  --navy-dark:#16263f;
  --nav:#22395d;
  --heading:#1f4f8f;
  --link:#3d6fb0;
  --btn:#8fbcd9;
  --text:#444a52;
  --line:#d9dee4;
  --grey-band:#dedede;
  --light:#e9e9e9;
  --orange:#f07c22;
  --white:#fff;
}
*{box-sizing:border-box;margin:0;padding:0}
html,body{width:1200px;height:2894px;overflow:hidden}
body{font-family:"Roboto",Arial,sans-serif;color:var(--text);background:var(--white);position:relative}
h1,h2,h3,h4{font-family:"Poppins",Arial,sans-serif}
a{color:inherit;text-decoration:none}

/* header */
.site-header{position:absolute;left:0;top:0;width:1200px;height:89px;background:linear-gradient(#1f3556,#1a2d4b)}
.site-name{position:absolute;left:73px;top:30px;font-family:"Poppins",sans-serif;font-weight:600;font-size:24px;color:var(--white)}
.search{position:absolute;left:794px;top:24px;width:334px;height:42px;display:flex}
.search input{flex:1;border:0;background:var(--white);font:14px "Roboto",sans-serif;padding:0 14px;color:#555}
.search button{width:38px;border:0;background:#5a8cc0;display:flex;align-items:center;justify-content:center}
.main-nav{position:absolute;left:0;top:89px;width:1200px;height:42px;background:var(--nav)}
.main-nav ul{list-style:none;display:flex;position:absolute;left:73px;top:0;height:42px}
.main-nav li{font-size:15px;color:var(--white);line-height:42px;padding:0 18px;border-right:1px solid #34507a;text-transform:uppercase}
.social-top{position:absolute;right:72px;top:10px;display:flex;gap:4px}
.social-top span{width:26px;height:26px;border-radius:50%;background:#e9edf2}

/* hero */
.hero{position:absolute;left:0;top:131px;width:1200px;height:488px;background:linear-gradient(180deg,#6d7f91 0%,#a98e6c 40%,#c88a4c 55%,#6d6a63 75%,#4f5660 100%)}
.hero-arrow{position:absolute;top:219px;width:34px;height:54px;background:rgba(20,30,45,.75);display:flex;align-items:center;justify-content:center}
.hero-arrow.left{left:0}.hero-arrow.right{right:0}
.wx-card{position:absolute;left:73px;width:451px;background:rgba(40,70,110,.72);border:2px solid rgba(160,190,220,.6);border-radius:6px;color:var(--white);overflow:hidden}
.wx-card .city{font-size:24px;position:absolute;left:20px}
.wx-card .temp{font-size:54px;position:absolute;left:20px}
.wx-now{height:182px}
.wx-now .city{top:10px}
.wx-now .temp{top:46px}
.wx-now .days{position:absolute;left:0;bottom:0;width:100%;height:44px;display:flex;background:rgba(90,130,175,.85);border-top:2px solid rgba(160,190,220,.6)}
.wx-now .days div{flex:1;text-align:center;line-height:42px;font-size:21px}
.wx-now .days div+div{border-left:2px solid rgba(160,190,220,.6)}
.wx-week{height:182px}
.wx-week .city{top:12px}
.wx-week .temp{top:8px;left:152px;font-size:42px}
.wx-week .range{position:absolute;left:20px;top:52px;font-size:18px}
.wx-week .days{position:absolute;left:0;bottom:0;width:100%;height:92px;display:flex;background:rgba(90,130,175,.85);border-top:2px solid rgba(160,190,220,.6)}
.wx-week .days div{flex:1;text-align:center;font-size:16px;padding-top:4px}
.wx-week .days div+div{border-left:1px solid rgba(160,190,220,.6)}
.wx-week .days svg{display:block;margin:4px auto}
.wx-icon{position:absolute}

/* common */
.section-title{font-weight:600;font-size:23px;color:var(--heading)}
.btn{display:inline-block;background:var(--btn);color:var(--white);font-size:13px;padding:0 13px;height:34px;line-height:34px}
p{font-size:13.5px;line-height:24px}

/* ad slots */
.ad-slot{position:absolute;width:278px;height:230px;background:linear-gradient(160deg,#1a4f9c,#0f3a7c);border:1px solid #c9d3df}

/* welcome */
.welcome{position:absolute;left:0;top:619px;width:1200px;height:325px}
.welcome h2{position:absolute;left:73px;top:42px}
.welcome p{position:absolute;left:73px;top:83px;width:700px;font-size:13px}
.welcome .btn{position:absolute;left:73px;top:225px}

/* videos */
.videos{position:absolute;left:0;top:944px;width:1200px;height:431px;background:linear-gradient(180deg,#4a6485 0%,#6e8aa8 45%,#3f5a7b 100%)}
.videos h2{position:absolute;width:100%;top:38px;text-align:center;color:var(--white);font-size:22px;font-weight:600}
.video-card{position:absolute;top:89px;width:333px}
.video-card .thumb{height:186px;background:linear-gradient(#55606c,#2b333b);display:flex;align-items:center;justify-content:center}
.video-card h3{font-family:"Roboto",sans-serif;font-weight:700;color:var(--white);font-size:14.5px;line-height:24px;margin-top:16px}
.video-card .btn{margin-top:16px;padding:0 19px}

/* stories */
.stories{position:absolute;left:0;top:1375px;width:1200px;height:455px}
.col-latest{position:absolute;left:73px;top:44px;width:280px}
.col-features{position:absolute;left:434px;top:44px;width:334px}
.stories h2{font-size:22px;margin-bottom:14px}
.story-link{font-size:13px;line-height:22px;color:var(--link);font-weight:500}
.story{margin-bottom:22px}
.story p{margin-top:6px;font-size:13px;line-height:22px}
.feature-list{list-style:none}
.feature-list li{font-size:15px;line-height:24px;color:var(--link);padding:4px 0 10px;border-bottom:1px solid var(--line);margin-bottom:8px}
.feature-list li:last-child{border-bottom:0}
.stories .btn{margin-top:6px}

/* banner band */
.band{position:absolute;left:0;top:1830px;width:1200px;height:120px;background:var(--grey-band)}
.banner-slot{position:absolute;left:265px;top:21px;width:673px;height:79px;background:linear-gradient(90deg,#e8edf3 0 155px,#123f86 155px,#1b5bb3)}

/* pictures + news */
.gallery-wrap{position:absolute;left:0;top:1950px;width:1200px;height:448px;background:var(--white);overflow:hidden}
.gallery-wrap .diag{position:absolute;inset:0}
.pics{position:absolute;left:73px;top:75px;width:732px;height:327px;background:#6e93bd}
.pics-tab{position:absolute;z-index:2;left:300px;top:44px;height:40px;padding:0 22px;background:#6e93bd;border-radius:8px 8px 0 0;color:var(--white);font-family:"Poppins",sans-serif;font-weight:600;font-size:21px;line-height:42px}
.pics-grid{position:absolute;left:14px;top:26px;display:grid;grid-template-columns:repeat(3,230px);grid-auto-rows:130px;gap:4px}
.pics-grid div{background:linear-gradient(#b7c3cc,#6b7c88)}
.pics-more{position:absolute;right:18px;bottom:8px;color:var(--white);font-size:14px;display:flex;align-items:center;gap:6px}
.news{position:absolute;left:832px;top:55px;width:300px}
.news h2{font-size:22px;margin-bottom:18px}
.news-item{display:flex;gap:16px;margin-bottom:18px}
.date{width:54px;height:60px;background:var(--navy);color:var(--white);text-align:center;flex:none}
.date b{display:block;font-size:24px;line-height:34px;font-family:"Poppins",sans-serif}
.date span{font-size:11px}
.news-item p{font-size:13px;line-height:22px;margin-top:4px}
.news-item p a{color:var(--link)}

/* newsletter */
.signup{position:absolute;left:0;top:2398px;width:1200px;height:213px;background:linear-gradient(180deg,#23324a 0%,#4a6380 45%,#6f8d4e 70%,#4a7a2a 100%)}
.signup h2{position:absolute;width:100%;top:38px;text-align:center;color:var(--white);font-weight:600;font-size:24px}
.signup .rule{position:absolute;top:54px;width:165px;height:2px;background:var(--white)}
.signup p{position:absolute;width:100%;top:77px;text-align:center;color:var(--white);font-size:22px}
.signup form{position:absolute;left:204px;top:113px;width:792px;height:62px;background:rgba(60,70,60,.75);padding:9px}
.signup .fields{display:flex;height:44px}
.signup input{border:0;background:#ededed;font:13px "Roboto",sans-serif;padding:0 16px;color:#777}
.signup input.name{width:335px;border-right:1px solid #ccc}
.signup input.email{width:335px}
.signup button{flex:1;border:0;background:var(--orange);color:var(--white);font:700 13px "Roboto",sans-serif}

/* footer */
.site-footer{position:absolute;left:0;top:2611px;width:1200px;height:247px;background:var(--navy)}
.fcol{position:absolute;top:28px;color:#d3dbe6}
.fcol h4{font-size:13px;color:var(--white);font-weight:600;letter-spacing:.5px;margin-bottom:20px}
.fcol ul{list-style:none}
.links li{font-size:13px;line-height:28px}
.contact li{font-size:13px;line-height:22px;display:flex;gap:14px;margin-bottom:14px}
.contact li svg{flex:none;margin-top:5px}
.quick input,.quick textarea{display:block;width:244px;border:0;background:var(--white);font:12px "Roboto",sans-serif;color:#555;padding:0 6px;height:24px;margin-bottom:4px}
.quick textarea{height:42px;padding-top:4px;resize:none}
.quick button{width:244px;height:24px;border:0;background:var(--orange);color:var(--white);font:700 12px "Roboto",sans-serif}
.connect li{display:flex;align-items:center;gap:12px;font-size:13px;margin-bottom:10px}
.connect li i{width:28px;height:28px;border-radius:50%;background:#eef1f5}
.copyright{position:absolute;left:0;top:2858px;width:1200px;height:36px;background:var(--navy-dark);color:#d0d8e3;font-size:13px;text-align:center;line-height:36px}
</style>
</head>
<body>

<header class="site-header">
  <div class="site-name">A WEATHER FORECASTING</div>
  <form class="search">
    <input type="text" value="Site Serach" aria-label="Site search">
    <button type="button" aria-label="Search">
      <svg width="18" height="18" viewBox="0 0 18 18"><circle cx="7.5" cy="7.5" r="5.5" fill="none" stroke="#fff" stroke-width="2"/><line x1="11.5" y1="11.5" x2="16" y2="16" stroke="#fff" stroke-width="2"/></svg>
    </button>
  </form>
</header>

<nav class="main-nav">
  <ul>
    <li>Home</li><li>Weather</li><li>Maps</li><li>Videos</li><li>Photos</li><li>Contacts</li>
  </ul>
  <div class="social-top"><span></span><span></span><span></span><span></span></div>
</nav>

<section class="hero" role="img" aria-label="City skyline at sunset with sun rays over downtown towers">
  <div class="hero-arrow left"><svg width="12" height="22"><polyline points="10,2 2,11 10,20" fill="none" stroke="#fff" stroke-width="2"/></svg></div>
  <div class="hero-arrow right"><svg width="12" height="22"><polyline points="2,2 10,11 2,20" fill="none" stroke="#fff" stroke-width="2"/></svg></div>

  <div class="wx-card wx-now" style="top:49px">
    <div class="city">City Name</div>
    <div class="temp">25°C</div>
    <svg class="wx-icon" style="left:262px;top:-6px" width="180" height="130" viewBox="0 0 180 130">
      <circle cx="95" cy="55" r="32" fill="#f7b51c"/>
      <g stroke="#f7b51c" stroke-width="6" stroke-linecap="round">
        <line x1="95" y1="5" x2="95" y2="15"/><line x1="135" y1="20" x2="128" y2="27"/><line x1="145" y1="55" x2="135" y2="55"/><line x1="55" y1="20" x2="62" y2="27"/><line x1="45" y1="55" x2="55" y2="55"/>
      </g>
      <path d="M30 120 a22 22 0 0 1 8-42 a30 30 0 0 1 56-10 a26 26 0 0 1 46 20 a18 18 0 0 1 -2 32 z" fill="#f2f5f8"/>
    </svg>
    <div class="days"><div>Monday</div><div>Cloudy</div></div>
  </div>

  <div class="wx-card wx-week" style="top:261px">
    <div class="city">City Name</div>
    <div class="temp">25°C</div>
    <div class="range">▲27° ▼20°</div>
    <svg class="wx-icon" style="left:320px;top:-4px" width="130" height="96" viewBox="0 0 180 130">
      <circle cx="95" cy="55" r="32" fill="#f7b51c"/>
      <path d="M30 120 a22 22 0 0 1 8-42 a30 30 0 0 1 56-10 a26 26 0 0 1 46 20 a18 18 0 0 1 -2 32 z" fill="#f2f5f8"/>
    </svg>
    <div class="days">
      <div>Mon<svg width="38" height="26" viewBox="0 0 38 26"><circle cx="22" cy="10" r="8" fill="#f7b51c"/><path d="M6 24 a7 7 0 0 1 4-12 a9 9 0 0 1 16 2 a6 6 0 0 1 2 10z" fill="#eef2f6"/></svg>25°</div>
      <div>Tue<svg width="38" height="26" viewBox="0 0 38 26"><circle cx="19" cy="13" r="9" fill="#f7b51c"/></svg>29°</div>
      <div>Wed<svg width="38" height="26" viewBox="0 0 38 26"><circle cx="19" cy="13" r="9" fill="#f7b51c"/></svg>30°</div>
      <div>Thu<svg width="38" height="26" viewBox="0 0 38 26"><circle cx="22" cy="10" r="8" fill="#f7b51c"/><path d="M6 24 a7 7 0 0 1 4-12 a9 9 0 0 1 16 2 a6 6 0 0 1 2 10z" fill="#eef2f6"/></svg>23°</div>
      <div>Fri<svg width="38" height="26" viewBox="0 0 38 26"><circle cx="22" cy="10" r="8" fill="#f7b51c"/><path d="M6 24 a7 7 0 0 1 4-12 a9 9 0 0 1 16 2 a6 6 0 0 1 2 10z" fill="#eef2f6"/></svg>22°</div>
      <div>Sat<svg width="38" height="26" viewBox="0 0 38 26"><path d="M8 18 a7 7 0 0 1 4-12 a9 9 0 0 1 16 2 a6 6 0 0 1 2 10z" fill="#eef2f6"/><g fill="#cfe3f7"><circle cx="13" cy="23" r="1.6"/><circle cx="19" cy="23" r="1.6"/><circle cx="25" cy="23" r="1.6"/></g></svg>25°</div>
    </div>
  </div>
</section>

<section class="welcome">
  <h2 class="section-title">Welcome to A Weather Forecasting</h2>
  <p>Lorem ipsum dolor sit amet, consectetur adipiscing elit, sed do eiusmod tempor incididunt ut labore et dolore magna aliqua. Ut enim ad minim veniam, quis nostrud exercitation ullamco laboris nisi ut aliquip ex ea commodo consequat. Duis aute irure dolor in reprehenderit in voluptate velit esse cillum dolore eu fugiat nulla pariatur. Excepteur sint occaecat cupidatat non proident, sunt in culpa qui officia deserunt mollit anim id est laborum."</p>
  <a class="btn">Read More</a>
  <aside class="ad-slot" style="left:841px;top:48px" role="img" aria-label="Advertisement space"></aside>
</section>

<section class="videos" aria-label="Forecast videos">
  <h2>Forecast Videos</h2>
  <article class="video-card" style="left:73px">
    <div class="thumb" role="img" aria-label="Supercell storm cloud over open plains"><svg width="42" height="42"><circle cx="21" cy="21" r="19" fill="none" stroke="#fff" stroke-width="2"/><polygon points="16,12 30,21 16,30" fill="none" stroke="#fff" stroke-width="2"/></svg></div>
    <h3>Lorem ipsum dolor sit amet, consectetur adipiscing elit,</h3>
    <a class="btn">More</a>
  </article>
  <article class="video-card" style="left:434px">
    <div class="thumb" role="img" aria-label="Forecast presenter beside a hurricane satellite view"><svg width="42" height="42"><circle cx="21" cy="21" r="19" fill="none" stroke="#fff" stroke-width="2"/><polygon points="16,12 30,21 16,30" fill="none" stroke="#fff" stroke-width="2"/></svg></div>
    <h3>Lorem ipsum dolor sit amet, consectetur adipiscing elit,</h3>
    <a class="btn">More</a>
  </article>
  <article class="video-card" style="left:795px">
    <div class="thumb" role="img" aria-label="Weather station instruments and anemometer"><svg width="42" height="42"><circle cx="21" cy="21" r="19" fill="none" stroke="#fff" stroke-width="2"/><polygon points="16,12 30,21 16,30" fill="none" stroke="#fff" stroke-width="2"/></svg></div>
    <h3>Lorem ipsum dolor sit amet, consectetur adipiscing elit,</h3>
    <a class="btn">More</a>
  </article>
</section>

<section class="stories">
  <div class="col-latest">
    <h2 class="section-title">Latest Stories</h2>
    <div class="story">
      <div class="story-link">Lorem ipsum dolor sit amet, consectetur<br>adipiscing elit,</div>
      <p>Sed ut perspiciatis unde omnis iste natus error sit voluptatem accusantium doloremque laudantium, totam rem aperiam.</p>
    </div>
    <div class="story">
      <div class="story-link">Lorem ipsum dolor sit amet, consectetur<br>adipiscing elit,</div>
      <p>Sed ut perspiciatis unde omnis iste natus error sit voluptatem accusantium doloremque laudantium, totam rem aperiam.</p>
    </div>
    <a class="btn">Read More</a>
  </div>
  <div class="col-features">
    <h2 class="section-title">Features &amp; Analysis</h2>
    <ul class="feature-list">
      <li>Lorem ipsum dolor sit amet, consectetur adipiscing elit.</li>
      <li>Phasellus ornare risus vitae ornare aliquet.</li>
      <li>Mauris finibus arcu porta sapien tincidunt laoreet.</li>
      <li>Lorem ipsum dolor sit amet, consectetur adipiscing elit.</li>
      <li>Phasellus ornare risus vitae ornare aliquet.</li>
    </ul>
    <a class="btn">Read More</a>
  </div>
  <aside class="ad-slot" style="left:841px;top:44px" role="img" aria-label="Advertisement space"></aside>
</section>

<section class="band">
  <div class="banner-slot" role="img" aria-label="Banner advertisement space"></div>
</section>

<section class="gallery-wrap">
  <svg class="diag" width="1200" height="448"><polygon points="740,0 1200,0 1200,448 530,448" fill="#e9e9e9"/></svg>
  <div class="pics-tab">Weather In Pictures</div>
  <div class="pics">
    <div class="pics-grid">
      <div role="img" aria-label="Hiker in a blue rain jacket"></div>
      <div role="img" aria-label="Colourful umbrella in the rain"></div>
      <div role="img" aria-label="People walking through a snowstorm"></div>
      <div role="img" aria-label="Dark storm clouds over green fields"></div>
      <div role="img" aria-label="Cars stuck in snowy traffic"></div>
      <div role="img" aria-label="Sunlit snowy boardwalk"></div>
    </div>
    <div class="pics-more">More Pictures <svg width="20" height="10"><line x1="0" y1="5" x2="18" y2="5" stroke="#fff" stroke-width="1.5"/><polyline points="13,1 18,5 13,9" fill="none" stroke="#fff" stroke-width="1.5"/></svg></div>
  </div>
  <div class="news">
    <h2 class="section-title">Fresh Weather News</h2>
    <div class="news-item">
      <div class="date"><b>06</b><span>Apr</span></div>
      <div><div class="story-link">Lorem ipsum dolor sit amet, consectetur adipiscing elit,</div><p>Sed ut perspiciatis unde omnis iste natus error sit voluptatem accusantium... <a>Read More</a></p></div>
    </div>
    <div class="news-item">
      <div class="date"><b>02</b><span>Apr</span></div>
      <div><div class="story-link">Lorem ipsum dolor sit amet, consectetur adipiscing elit,</div><p>Sed ut perspiciatis unde omnis iste natus error sit voluptatem accusantium... <a>Read More</a></p></div>
    </div>
    <a class="btn">Read More</a>
  </div>
</section>

<section class="signup" aria-label="Newsletter signup">
  <span class="rule" style="left:345px"></span>
  <h2>Get Updated!</h2>
  <span class="rule" style="left:690px"></span>
  <p>Sign Up for free newsletter today.</p>
  <form>
    <div class="fields">
      <input class="name" type="text" value="Name" aria-label="Name">
      <input class="email" type="text" value="Email Address" aria-label="Email address">
      <button type="button">SUBMIT</button>
    </div>
  </form>
</section>

<footer class="site-footer">
  <div class="fcol links" style="left:73px">
    <h4>QUICK LINKS</h4>
    <ul><li>HOME</li><li>WEATHER</li><li>MAPS</li><li>VIDEOS</li><li>PHOTOS</li><li>CONTACTS</li></ul>
  </div>
  <div class="fcol contact" style="left:344px;width:250px">
    <h4>CONTACT US</h4>
    <ul>
      <li><svg width="12" height="12" viewBox="0 0 12 12"><path d="M2 1 l3 0 l1 3 l-2 1 a7 7 0 0 0 3 3 l1-2 l3 1 l0 3 a10 10 0 0 1 -9 -9z" fill="#fff"/></svg>+1 000 000 00 00</li>
      <li><svg width="13" height="10" viewBox="0 0 13 10"><rect x="0.5" y="0.5" width="12" height="9" fill="#fff"/><polyline points="1,1 6.5,5.5 12,1" fill="none" stroke="#1c3050"/></svg>info@skyline-forecast.com</li>
      <li><svg width="11" height="14" viewBox="0 0 11 14"><path d="M5.5 14 C1 8 0 7 0 5.5 a5.5 5.5 0 0 1 11 0 c0 1.5-1 2.5-5.5 8.5z" fill="#fff"/><circle cx="5.5" cy="5.5" r="2" fill="#1c3050"/></svg>Weather Forecasting<br>Lorem ipsum dolor sit amet<br>WA, 32568</li>
    </ul>
  </div>
  <div class="fcol quick" style="left:615px">
    <h4>QUICK CONTACT</h4>
    <input type="text" value="Name" aria-label="Name">
    <input type="text" value="Email" aria-label="Email">
    <input type="text" value="Phone" aria-label="Phone">
    <textarea aria-label="Message">Message</textarea>
    <button type="button">SUBMIT</button>
  </div>
  <div class="fcol connect" style="left:884px">
    <h4>CONNECT WITH US</h4>
    <ul><li><i></i>Friendbook</li><li><i></i>Chirper</li><li><i></i>Circles+</li><li><i></i>ViewTube</li></ul>
  </div>
</footer>
<div class="copyright">© 2017 Weather Forecasting. All Rights Reserved. | Terms &amp; Conditions</div>

</body>
</html>
```